Flock and co fleece works pty ltd

We are sheep shearing contractors,we are looking for a simple design business card, with a drawing like picture of a Australian sheep on it, then just standard details, name, phone, email, po box.
We would like double sided, with 2 lines of wiriting on the back, no bright colours please.
We like black and white, doesn't have to be too serious, however nothing to far left of cwntre.
On the back of the card we would like professional shearing contract offering full contract team.
Can use use the symbol & in the name instead of and.

Target Market(s)

Sheep farmers, target males from age 20 and up

Contact Information for Business Card

Company name flock and co fleece works pty ltd
Darren holloway 0491352706, po box 4071 sale vic 3853,
Email flockandcofleece@mailbarn.example, gippsland shearing contractor

Font styles to use
Serif

Colors

Designer to choose only greyscale colors for use in the design.

Requirements
Nice to have
• Simple design

```html
<!DOCTYPE html>
<html lang="en">
<head>
<meta charset="utf-8">
<title>Flock and Co Fleece Works – Business Card</title>
<link rel="stylesheet" href="https://fonts.googleapis.com/css2?family=Archivo+Black&family=Arimo:wght@400;700&display=swap">
<style>
  :root {
    --page: #2a2a2a;
    --paper: #ffffff;
    --ink: #111111;
    --card-dark: #1d1d1d;
    --sheep-tone-a: #0c0c0c;
    --sheep-tone-b: #161616;
    --rule-light: #9a9a9a;
    --text-light: #e4e4e4;
    --text-white: #ffffff;
  }
  * { box-sizing: border-box; margin: 0; padding: 0; }
  html, body { width: 1200px; height: 900px; overflow: hidden; }
  body {
    background: var(--page);
    font-family: "Arimo", Arial, sans-serif;
    position: relative;
  }
  .card {
    position: absolute;
    left: 290px;
    width: 620px;
    height: 378px;
    overflow: hidden;
    box-shadow: 0 10px 30px rgba(0,0,0,.5);
  }
  .wordmark {
    text-transform: uppercase;
    line-height: 1;
    white-space: nowrap;
  }
  .wordmark__main {
    display: block;
    font-family: "Archivo Black", "Arial Black", sans-serif;
    font-size: 46px;
    letter-spacing: 1px;
  }
  .wordmark__sub {
    display: block;
    font-family: "Arimo", Arial, sans-serif;
    font-size: 24px;
    letter-spacing: .5px;
    margin-top: 2px;
  }
  .wordmark__suffix { font-size: 16px; letter-spacing: .5px; }

  /* Back side (white) */
  .card--back { top: 42px; background: var(--paper); color: var(--ink); }
  .card--back .wordmark { position: absolute; left: 110px; top: 48px; }
  .back__band-top {
    position: absolute; left: 0; top: 140px; width: 100%; height: 10px;
    background: var(--ink);
  }
  .back__role {
    position: absolute; left: 150px; right: 24px; top: 160px;
    font-size: 19px; text-transform: uppercase; letter-spacing: .5px;
    text-align: right;
  }
  .back__write-line {
    position: absolute; left: 150px; width: 360px; height: 1px;
    background: var(--rule-light);
  }
  .back__write-line--one { top: 226px; }
  .back__write-line--two { top: 276px; }
  .back__band-tagline {
    position: absolute; left: 0; top: 314px; width: 100%; height: 42px;
    background: var(--ink); color: var(--text-white);
    font-size: 18px; display: flex; align-items: center; justify-content: center;
  }

  /* Front side (dark) */
  .card--front { top: 472px; background: var(--card-dark); color: var(--text-light); }
  .front__sheep { position: absolute; left: 60px; top: 18px; width: 470px; height: 342px; }
  .card--front .wordmark { position: absolute; left: 110px; top: 70px; color: var(--text-light); }
  .front__details {
    position: absolute; left: 150px; top: 180px; width: 330px;
    text-align: center; color: var(--text-white);
  }
  .front__name {
    font-family: "Archivo Black", "Arial Black", sans-serif;
    font-size: 22px; text-transform: uppercase; letter-spacing: .5px;
  }
  .front__rule { width: 150px; height: 1px; background: var(--rule-light); margin: 10px auto; }
  .front__line { font-size: 18px; line-height: 1.35; }
</style>
</head>
<body>

<section class="card card--back" aria-label="Card back">
  <div class="wordmark">
    <span class="wordmark__main">Flock and Co</span>
    <span class="wordmark__sub">Fleece Works <span class="wordmark__suffix">Pty Ltd</span></span>
  </div>
  <div class="back__band-top"></div>
  <p class="back__role">Gippsland Shearing Contractor</p>
  <div class="back__write-line back__write-line--one"></div>
  <div class="back__write-line back__write-line--two"></div>
  <p class="back__band-tagline">Professional shearing contract offering full contract team.</p>
</section>

<section class="card card--front" aria-label="Card front">
  <svg class="front__sheep" viewBox="0 0 470 342" role="img" aria-label="Engraved-style illustration of a horned Australian sheep standing in profile">
    <defs>
      <linearGradient id="sheepTone" x1="0" y1="0" x2="1" y2="1">
        <stop offset="0" stop-color="var(--sheep-tone-a)"/>
        <stop offset="1" stop-color="var(--sheep-tone-b)"/>
      </linearGradient>
    </defs>
    <rect x="0" y="0" width="470" height="342" rx="60" fill="url(#sheepTone)" opacity=".8"/>
  </svg>
  <div class="wordmark">
    <span class="wordmark__main">Flock and Co</span>
    <span class="wordmark__sub">Fleece Works <span class="wordmark__suffix">Pty Ltd</span></span>
  </div>
  <div class="front__details">
    <p class="front__name">Darren Holloway</p>
    <div class="front__rule"></div>
    <p class="front__line">0491352706</p>
    <p class="front__line">flockandcofleece@mailbarn.example</p>
    <div class="front__rule"></div>
    <p class="front__line">PO box 4071 sale vic 3853</p>
  </div>
</section>

</body>
</html>
```